Wandelow valley aerial works business card size advertising

I’m after a simple design , please see attached photo . Im after the same color green in the photo as the base color and the the little white man but instead of him holding a spanner i would like him to be holding a tv antenna pointing an angle , see attached photo of the antenna , i would like him on the left of the business card and the business name to fit in on the right with the phone number . ( if the antenna idea looks stupid , leave him holding a spanner ) On the reverse side of the card i would like a white background with green writing stating some of the services we provide which are the following .Antenna installations and repairs Wall mounting of tv’s Additional TV outlets Orbix satellite supply and installations Wandelow , Brackenfield , Tarrowee , Moorinda , Kelvara , Collector , All rural areas All in all i would like the business card to compliment my invoices as pictured “ invoice supplied is a dummy invoice “

wandelow valley aerial works 0491836527

Sans Serif

9bcb3c

• what i ask for in project description

```html
<!DOCTYPE html>
<html lang="en">
<head>
<meta charset="utf-8">
<title>Wandelow Valley Aerial Works – Business Card</title>
<link rel="stylesheet" href="https://fonts.googleapis.com/css2?family=Quicksand:wght@700&family=Teko:wght@500;600&display=swap">
<style>
  :root {
    --brand-green: #9bcb3c;
    --paper-white: #ffffff;
    --band-light: #f2f2f2;
    --figure-tint: #cfe69a;
    --backdrop: #2b2b2b;
  }
  * { margin: 0; padding: 0; box-sizing: border-box; }
  html, body { width: 1200px; height: 900px; overflow: hidden; }
  body { background: var(--backdrop); position: relative; }

  .card {
    position: absolute;
    left: 261px;
    width: 656px;
    height: 358px;
    overflow: hidden;
  }
  .card-front { top: 69px; background: var(--brand-green); }
  .card-back  { top: 472px; background: var(--paper-white); }

  .phone-band {
    position: absolute;
    left: 121px; right: 0; top: 294px; bottom: 0;
    background: var(--band-light);
  }
  .mascot-area {
    position: absolute;
    left: 0; top: 0;
    width: 656px; height: 358px;
  }
  .business-name {
    position: absolute;
    left: 217px;
    top: 118px;
    width: 410px;
    color: var(--band-light);
    font-family: "Teko", sans-serif;
    text-transform: uppercase;
    line-height: 1;
    white-space: nowrap;
  }
  .business-name .name-line-1 {
    display: block;
    font-weight: 600;
    font-size: 52px;
    letter-spacing: 2px;
  }
  .business-name .name-line-2 {
    display: block;
    margin-top: 6px;
    font-weight: 600;
    font-size: 46px;
    letter-spacing: 12px;
  }
  .phone-number {
    position: absolute;
    right: 34px;
    top: 300px;
    color: var(--brand-green);
    font-family: "Quicksand", sans-serif;
    font-weight: 700;
    font-size: 50px;
    letter-spacing: 8px;
    line-height: 1.2;
    white-space: nowrap;
  }

  .service-areas {
    position: absolute;
    left: 0; right: 0; top: 142px;
    padding: 0 60px;
    text-align: center;
    color: var(--brand-green);
    font-family: "Teko", sans-serif;
    font-weight: 500;
    text-transform: uppercase;
    font-size: 30px;
    letter-spacing: 0.5px;
    line-height: 45px;
    white-space: nowrap;
  }
</style>
</head>
<body>
  <section class="card card-front">
    <div class="phone-band"></div>
    <svg class="mascot-area" viewBox="0 0 656 358" role="img" aria-label="White pictogram man standing on the left, holding up a tall TV antenna mast">
      <rect x="18" y="20" width="181" height="338" fill="var(--figure-tint)"/>
      <rect x="199" y="20" width="286" height="81" fill="var(--figure-tint)"/>
    </svg>
    <h1 class="business-name">
      <span class="name-line-1">Wandelow Valley</span>
      <span class="name-line-2">Aerial Works</span>
    </h1>
    <p class="phone-number">0491836527</p>
  </section>

  <section class="card card-back">
    <p class="service-areas">
      Antenna installations Wandelow<br>
      Brackenfield | Tarrowee | Moorinda | Kelvara
    </p>
  </section>
</body>
</html>
```